We need a modern Google Slides/ PowerPoint presentation for our business brokerage firm in California. Please see attached design colors for colors and fonts- primary colors: white, blue & yellow. On the cover slide we want our logo to be white on blue background (I do not have our logo in white yet, so you can just leave place for logo.) Please limit the amount of stock photos with people. We will insert "Team" photos ourselves, just leave a place for them. Content is attached. Thank you!

```html
<!DOCTYPE html>
<html lang="en">
<head>
<meta charset="utf-8">
<title>Keystone Business Advisors — Presentation</title>
<link href="https://fonts.googleapis.com/css2?family=Poppins:wght@300;400;500;600;700&family=Open+Sans:wght@400;600;700&display=swap" rel="stylesheet">
<style>
:root{
  --navy:#15315e;
  --navy-deep:#0f2448;
  --yellow:#ffec00;
  --gold:#c9b600;
  --white:#ffffff;
  --ink:#2b2b2b;
  --muted:#5a5a5a;
  --red:#d71920;
  --green:#6cb33f;
  --sky:#1aa3e0;
  --page:#000000;
}
*{box-sizing:border-box;margin:0;padding:0}
html,body{width:1200px;height:2736px;overflow:hidden;background:var(--page)}
body{position:relative;font-family:"Open Sans",Arial,sans-serif;color:var(--ink)}
.slide{position:absolute;width:540px;height:304px;overflow:hidden;background:var(--white)}
.abs{position:absolute}
.col-l{left:45px}.col-r{left:615px}
.row1{top:48px}.row2{top:381px}.row3{top:715px}.row4{top:1048px}.row5{top:1382px}.row6{top:1715px}.row7{top:2048px}
.slide-contact{top:2382px;left:330px;background:var(--navy)}
.shapes{position:absolute;left:0;top:0}
.photo{position:absolute}
.h-display{font-family:"Poppins",sans-serif;font-weight:700;letter-spacing:-.5px;line-height:1.05}
.h-light{font-family:"Poppins",sans-serif;font-weight:300}
.h-light b{font-weight:700}
.body{font-size:9.6px;line-height:1.16}
.logo{position:absolute;font-family:"Poppins",sans-serif;font-weight:600;color:var(--navy);line-height:1}
.logo .name{display:block;font-size:20px;letter-spacing:1.5px}
.logo .sub{display:block;font-size:7.4px;letter-spacing:1.2px;margin-top:2px}
.logo.small .name{font-size:13px;letter-spacing:1px}
.logo.small .sub{font-size:4.8px;letter-spacing:.8px;margin-top:1px}
.logo.white{color:var(--white)}
.pgno{position:absolute;right:14px;bottom:9px;font-size:5.5px;font-weight:700;color:var(--navy)}
.pgno.light{color:var(--white)}
.copy{position:absolute;font-size:5px;color:#8a8a8a}
.date{position:absolute;font-size:6.6px;color:var(--ink)}
/* covers */
.cover-title{position:absolute;left:28px;top:108px;font-size:24px;color:var(--white);width:260px}
.cover-title.accent{color:var(--yellow)}
.cover-title.dark{color:var(--navy)}
.cover-text{position:absolute;left:28px;top:168px;width:240px;font-size:9.4px;line-height:1.13;color:var(--white)}
.cover-text.dark{color:var(--navy)}
/* framework */
.fw-title{position:absolute;left:0;width:100%;top:20px;text-align:center;font-size:22px;color:var(--navy)}
.fw-sub{position:absolute;left:0;width:100%;top:53px;text-align:center;font-size:8.4px}
.fw-col{position:absolute;top:76px;width:74px}
.fw-tab{position:relative;height:20px}
.fw-tab .bar{position:absolute;left:6px;right:0;top:3px;height:14px;background:var(--yellow);border-radius:0 8px 8px 0}
.fw-tab .num{position:absolute;left:0;top:0;width:20px;height:20px;border-radius:50%;color:#fff;font:600 12px/20px "Poppins",sans-serif;text-align:center;border:2px solid #fff}
.fw-head{margin-top:4px;font-weight:700;font-size:8px;line-height:1.1;color:var(--navy);text-align:right;padding-right:6px}
.fw-text{margin-top:4px;font-size:5.4px;line-height:1.2;text-align:right;padding-right:6px;color:var(--ink)}
/* services */
.svc-top{position:absolute;left:0;top:0;width:540px;height:117px;background:var(--navy)}
.svc-title{position:absolute;left:0;width:100%;top:30px;text-align:center;font-size:20px;color:var(--white)}
.svc-title b{color:var(--yellow)}
.svc{position:absolute;top:88px;width:112px;text-align:center}
.svc .icon{width:54px;height:54px;margin:0 auto;border-radius:50%;border:3px solid #fff;box-shadow:0 1px 3px rgba(0,0,0,.3)}
.svc h3{margin-top:5px;font-size:10px;line-height:1.1;font-weight:700;color:var(--navy)}
.svc p{margin-top:9px;font-size:7.6px;line-height:1.16}
/* feature slides */
.feat-title{position:absolute;font-size:22px;color:var(--navy)}
.feat-title .amp{font-weight:400}
.feat-text{position:absolute;font-size:9.2px;line-height:1.15}
.feat-text p+p{margin-top:6px}
/* values */
.val-title{position:absolute;left:0;width:100%;top:20px;text-align:center;font-size:22px;color:var(--navy)}
.val-l{position:absolute;width:195px;text-align:right}
.val-r{position:absolute;width:200px;left:328px}
.val-l h4,.val-r h4{font-family:"Poppins",sans-serif;font-weight:400;font-size:12px;color:var(--ink)}
.val-l p,.val-r p{font-size:6.3px;line-height:1.2;margin-top:3px}
.val-icon{position:absolute;width:38px;height:38px;border-radius:50%}
/* team */
.team-title{position:absolute;left:0;width:100%;top:30px;text-align:center;font-size:20px;color:var(--white)}
.team-title b{color:var(--yellow)}
.member{position:absolute;top:78px;width:150px;text-align:center}
.member .portrait{width:72px;height:72px;margin:0 auto;border-radius:50%;border:3px solid #fff;background:radial-gradient(circle at 50% 40%,#c9cdd3,#7d858f)}
.member h4{margin-top:4px;font-family:"Poppins",sans-serif;font-weight:600;font-size:11px;color:var(--navy)}
.member .role{font-size:7.6px;margin-top:1px}
.member p{font-size:7.6px;line-height:1.18;margin-top:9px}
/* contact */
.ct-head{font-family:"Poppins",sans-serif;font-weight:600;font-size:12.6px;color:var(--white)}
.office{position:absolute;color:var(--white);font-size:7.4px;line-height:1.15}
.office h5{font-family:"Poppins",sans-serif;font-weight:600;font-size:10px;color:var(--yellow);margin-bottom:3px}
.office p+p{margin-top:8px}
</style>
</head>
<body>

<!-- Cover A -->
<section class="slide col-l row1">
  <svg class="shapes" width="540" height="304" viewBox="0 0 540 304">
    <rect x="0" y="88" width="490" height="145" fill="var(--navy)"/>
    <polygon points="418,37 449,37 449,69" fill="var(--gold)"/>
    <polygon points="447,37 540,37 540,104 470,104" fill="var(--yellow)"/>
    <polygon points="0,233 263,233 237,265 0,265" fill="var(--yellow)"/>
    <polygon points="225,233 263,233 245,265 215,265" fill="var(--gold)"/>
  </svg>
  <div class="photo" role="img" aria-label="Photo of a businessman signing a document with a pen" style="left:226px;top:69px;width:274px;height:181px;clip-path:polygon(0 0,100% 0,80% 100%,38% 100%);background:linear-gradient(135deg,#2b3a50,#8e8b86 55,#d8d2c8)"></div>
  <div class="logo" style="left:28px;top:34px"><span class="name">KEYSTONE</span><span class="sub">BUSINESS ADVISORS</span></div>
  <h1 class="cover-title h-display">We sell businesses more effectively</h1>
  <p class="cover-text">We are a full-service business brokerage &amp; M&amp;A advisory firm in California. With our proven strategic framework, we sell privately held businesses at a greater value and in less time.</p>
  <div class="date" style="left:27px;top:245px">Saturday, May 29, 2021</div>
  <div class="copy" style="right:28px;top:275px">© 2021 Keystone Business Advisors. All rights reserved.</div>
</section>

<!-- Cover B -->
<section class="slide col-r row1">
  <svg class="shapes" width="540" height="304" viewBox="0 0 540 304">
    <rect x="0" y="88" width="490" height="145" fill="var(--navy)"/>
    <polygon points="418,37 449,37 449,69" fill="var(--gold)"/>
    <polygon points="447,37 540,37 540,104 470,104" fill="var(--yellow)"/>
    <polygon points="0,233 263,233 237,265 0,265" fill="var(--yellow)"/>
    <polygon points="225,233 263,233 245,265 215,265" fill="var(--gold)"/>
  </svg>
  <div class="photo" role="img" aria-label="Photo of hands using a tablet at a desk" style="left:226px;top:69px;width:274px;height:181px;clip-path:polygon(0 0,100% 0,80% 100%,38% 100%);background:linear-gradient(135deg,#1f3a63,#7f8fa6 50%,#e4e6ea)"></div>
  <div class="logo" style="left:28px;top:34px"><span class="name">KEYSTONE</span><span class="sub">BUSINESS ADVISORS</span></div>
  <h1 class="cover-title accent h-display">We sell businesses more effectively</h1>
  <p class="cover-text">We are a full-service business brokerage &amp; M&amp;A advisory firm in California. With our proven strategic framework, we sell privately held businesses at a greater value and in less time.</p>
  <div class="date" style="left:27px;top:245px">Saturday, May 29, 2021</div>
  <div class="copy" style="right:28px;top:275px">© 2021 Keystone Business Advisors. All rights reserved.</div>
</section>

<!-- Cover C -->
<section class="slide col-l row2" style="background:var(--navy)">
  <svg class="shapes" width="540" height="304" viewBox="0 0 540 304">
    <rect x="0" y="88" width="540" height="145" fill="var(--white)"/>
    <polygon points="418,37 449,37 449,69" fill="var(--gold)"/>
    <polygon points="447,37 540,37 540,104 470,104" fill="var(--yellow)"/>
    <polygon points="0,233 263,233 237,265 0,265" fill="var(--yellow)"/>
    <polygon points="225,233 263,233 245,265 215,265" fill="var(--gold)"/>
  </svg>
  <div class="photo" role="img" aria-label="Aerial photo of a suspension bridge over the bay" style="left:226px;top:69px;width:314px;height:181px;clip-path:polygon(0 0,100% 0,100% 100%,33% 100%);background:linear-gradient(160deg,#c9b8a6,#8c9aa3 45%,#4f6a78)"></div>
  <div class="logo white" style="left:28px;top:34px"><span class="name">KEYSTONE</span><span class="sub">BUSINESS ADVISORS</span></div>
  <h1 class="cover-title dark h-display">We sell businesses more effectively</h1>
  <p class="cover-text dark">We are a full-service business brokerage &amp; M&amp;A advisory firm in California. With our proven strategic framework, we sell privately held businesses at a greater value and in less time.</p>
  <div class="date" style="left:27px;top:245px">Saturday, May 29, 2021</div>
  <div class="copy" style="right:28px;top:275px;color:#c9d1de">© 2021 Keystone Business Advisors. All rights reserved.</div>
</section>

<!-- Framework -->
<section class="slide col-r row2">
  <h2 class="fw-title h-light">Our <b>Framework</b></h2>
  <p class="fw-sub">We've helped hundreds of clients to sell their business at higher value by following our strategic framework.</p>
  <div class="fw-col" style="left:20px"><div class="fw-tab"><span class="bar"></span><span class="num" style="background:var(--red)">1</span></div><h3 class="fw-head">Preparation &amp; Planning</h3><p class="fw-text">This phase focuses on preparing your business for sale. We believe advanced preparation is key to success and makes your business more attractive to buyers.</p></div>
  <div class="fw-col" style="left:104px"><div class="fw-tab"><span class="bar"></span><span class="num" style="background:var(--green)">2</span></div><h3 class="fw-head">Business Valuation</h3><p class="fw-text">We will advise you on the best methods to determine the price range for your business, review key documents and the factors that drive value.</p></div>
  <div class="fw-col" style="left:189px"><div class="fw-tab"><span class="bar"></span><span class="num" style="background:var(--sky)">3</span></div><h3 class="fw-head">Marketing the Business</h3><p class="fw-text">Once we've set the price and sales strategy, we will prepare a marketing plan and promote your business to qualified buyers while keeping it confidential.</p></div>
  <div class="fw-col" style="left:274px"><div class="fw-tab"><span class="bar"></span><span class="num" style="background:var(--red)">4</span></div><h3 class="fw-head">Meet the buyer</h3><p class="fw-text">A non-disclosure agreement must be signed by all interested buyers. We only work with buyers who meet the appropriate financial requirements to make an offer.</p></div>
  <div class="fw-col" style="left:359px"><div class="fw-tab"><span class="bar"></span><span class="num" style="background:var(--green)">5</span></div><h3 class="fw-head">Offers &amp; Negotiations</h3><p class="fw-text">During this phase, our goal is to produce the best possible offer for your business. We will guide you through each offer and its terms.</p></div>
  <div class="fw-col" style="left:444px"><div class="fw-tab"><span class="bar"></span><span class="num" style="background:var(--sky)">6</span></div><h3 class="fw-head">Closing</h3><p class="fw-text">We will work closely with your CPA, landlord, attorney, and all relevant third parties to ensure a smooth closing.</p></div>
  <div class="logo small" style="left:14px;top:272px"><span class="name">KEYSTONE</span><span class="sub">BUSINESS ADVISORS</span></div>
  <span class="pgno">4</span>
</section>

<!-- What we do -->
<section class="slide col-l row3">
  <div class="svc-top"></div>
  <h2 class="svc-title h-light">What we <b>do...</b></h2>
  <div class="svc" style="left:40px">
    <svg class="icon" viewBox="0 0 54 54" style="background:var(--navy)"><path d="M17 25h5v13h-5z M24 25l5-9c2 0 3 1 3 3l-1 5h6c2 0 3 2 2 4l-3 9c-1 1-2 1-3 1H24z" fill="#fff"/></svg>
    <h3>Exit<br>Planning</h3><p>Exit planning strategy will identify the actions that need to be taken so that you can exit your business with confidence.</p></div>
  <div class="svc" style="left:156px">
    <svg class="icon" viewBox="0 0 54 54" style="background:var(--red)"><circle cx="27" cy="22" r="9" fill="#fff"/><rect x="23" y="30" width="8" height="7" rx="1" fill="#fff"/></svg>
    <h3>Business<br>Valuations</h3><p>By utilizing a variety of valuation methods, we will evaluate your business and determine the most probable selling price.</p></div>
  <div class="svc" style="left:272px">
    <svg class="icon" viewBox="0 0 54 54" style="background:var(--green)"><rect x="17" y="30" width="5" height="8" fill="#fff"/><rect x="24" y="25" width="5" height="13" fill="#fff"/><rect x="31" y="20" width="5" height="18" fill="#fff"/><path d="M16 26l9-7 5 3 8-7" stroke="#fff" stroke-width="2" fill="none"/></svg>
    <h3>Seller<br>Representation</h3><p>With our proven strategic framework, we'll help you to sell your business at a greater value and in less time</p></div>
  <div class="svc" style="left:389px">
    <svg class="icon" viewBox="0 0 54 54" style="background:var(--sky)"><path d="M19 15h16v6c0 5-4 9-8 9s-8-4-8-9z" fill="#fff"/><rect x="25" y="30" width="4" height="5" fill="#fff"/><rect x="20" y="35" width="14" height="3" fill="#fff"/></svg>
    <h3>Buyer<br>Representation</h3><p>From deal sourcing to closing, we guide business buyers through the entire process to set them up for success.</p></div>
  <div class="logo small" style="left:14px;top:272px"><span class="name">KEYSTONE</span><span class="sub">BUSINESS ADVISORS</span></div>
  <span class="pgno">5</span>
</section>

<!-- No upfront costs -->
<section class="slide col-r row3" style="background:var(--navy)">
  <div class="photo" role="img" aria-label="Faint navy-tinted photo of a bridge" style="inset:0;background:linear-gradient(170deg,#25426e,#1a3663 50%,#15315e)"></div>
  <div class="logo small white" style="left:226px;top:78px"><span class="name">KEYSTONE</span><span class="sub">BUSINESS ADVISORS</span></div>
  <h2 class="h-display abs" style="left:0;width:100%;top:128px;text-align:center;font-size:22px;color:var(--yellow)">We don't charge<br>upfront costs.</h2>
  <p class="body abs" style="left:135px;width:270px;top:190px;text-align:center;color:#fff;font-size:9.4px">We are able to deliver world class business brokerage services without upfront costs for our clients. Our fees are success-based. With a success-based pricing model, our commission is earned AFTER the business is sold.</p>
</section>

<!-- Preparation & Planning -->
<section class="slide col-l row4">
  <div class="photo" role="img" aria-label="Photo of a hand placing a dart on a target beside a laptop" style="left:37px;top:0;width:236px;height:238px;background:linear-gradient(160deg,#d8d5d0,#a7a39b 50%,#c89a2e 80%,#3a3a3a)"></div>
  <h2 class="feat-title h-display" style="left:313px;top:60px">Preparation <span class="amp">&amp;</span><br>Planning</h2>
  <p class="feat-text" style="left:313px;top:120px;width:180px">Advanced preparation is the key to success. We help you to prepare your business for sale before it goes on the market. Exit planning strategy will make your business more attractive to the potential buyers and allow you to maximize the value of your business.</p>
  <div class="logo small" style="left:14px;top:272px"><span class="name">KEYSTONE</span><span class="sub">BUSINESS ADVISORS</span></div>
  <span class="pgno">7</span>
</section>

<!-- Technology -->
<section class="slide col-r row4" style="background:var(--navy)">
  <div class="photo" role="img" aria-label="Photo of hands holding a tablet showing charts" style="left:0;top:0;width:540px;height:152px;background:linear-gradient(120deg,#a77a4e,#d9b993 40%,#e7ddd1 70%,#b79673)"></div>
  <h2 class="h-display abs" style="right:295px;top:187px;font-size:21px;color:var(--yellow);text-align:right">Technology<br>Driven Process</h2>
  <div class="abs" style="left:270px;top:172px;width:1px;height:82px;background:#6f86aa"></div>
  <p class="body abs" style="left:296px;top:186px;width:190px;color:#fff;font-size:9px">We have a proven, technology-driven process. It allows us to effectively manage the sales transaction from every angle and move the deal towards closing faster.</p>
  <div class="logo small white" style="left:14px;top:267px"><span class="name">KEYSTONE</span><span class="sub">BUSINESS ADVISORS</span></div>
  <span class="pgno light">8</span>
</section>

<!-- Local Market -->
<section class="slide col-l row5">
  <div class="photo" role="img" aria-label="Navy-tinted photo of business people shaking hands over a desk" style="left:0;top:0;width:270px;height:304px;background:linear-gradient(120deg,#1b3968,#2c4f83 45%,#a8b8cc 70%,#2a4676)"></div>
  <h2 class="feat-title h-display" style="left:312px;top:40px">Local Market <span class="amp">&amp;</span><br>Industry<br>Knowledge</h2>
  <div class="feat-text" style="left:312px;top:135px;width:185px"><p>We've been selling businesses in the Bay Area and Southern California for over 30 years. We know exactly how to effectively market your business in the local market and get it in front of the right buyers faster.</p><p>Our business brokers have a strong grasp of all that goes into the acquisition, operation, and sale of businesses.</p></div>
  <div class="logo small white" style="left:14px;top:262px"><span class="name">KEYSTONE</span><span class="sub">BUSINESS ADVISORS</span></div>
  <span class="pgno">9</span>
</section>

<!-- Integrity -->
<section class="slide col-r row5">
  <div class="abs" style="left:500px;top:0;width:40px;height:304px;background:var(--navy)"></div>
  <div class="abs" style="left:385px;top:245px;width:155px;height:59px;background:var(--navy)"></div>
  <div class="photo" role="img" aria-label="Photo of two business people shaking hands over a desk" style="left:267px;top:0;width:237px;height:246px;background:linear-gradient(140deg,#eef2f6,#aebdcc 45%,#6d7f95 75%,#d9dee4)"></div>
  <h2 class="feat-title h-display" style="left:36px;top:32px">Integrity,<br>Commitment <span class="amp">&amp;</span><br>Support</h2>
  <div class="feat-text" style="left:36px;top:122px;width:205px"><p>Our business model is built on transparency, integrity, and commitment. We are committed to the success of each of our clients.</p><p>The process of selling a business is complex and sometimes can be stressful.</p><p>We will be with you every step of the way from preparing business to go on the market to closing. We'll provide you with the attention and support that you deserve.</p></div>
  <div class="logo small" style="left:14px;top:264px"><span class="name">KEYSTONE</span><span class="sub">BUSINESS ADVISORS</span></div>
  <span class="pgno light">10</span>
</section>

<!-- Results -->
<section class="slide col-l row6">
  <div class="abs" style="left:405px;top:0;width:135px;height:304px;background:var(--navy)"></div>
  <div class="photo" role="img" aria-label="Photo of hands reviewing printed charts with a pen" style="left:222px;top:0;width:185px;height:304px;background:linear-gradient(160deg,#3a3a3c,#cfd2d6 40%,#eef0f2 65%,#8a9099)"></div>
  <h2 class="feat-title h-display" style="left:43px;top:40px">Results</h2>
  <p class="feat-text" style="left:43px;top:78px;width:140px">At the end of the day, this is about selling your business at the right price to the right buyer and that's what we do best! We have decades of experience and a proven track record of helping hundreds of business owners.</p>
  <div class="logo small" style="left:14px;top:267px"><span class="name">KEYSTONE</span><span class="sub">BUSINESS ADVISORS</span></div>
  <span class="pgno light">11</span>
</section>

<!-- Core Values -->
<section class="slide col-r row6">
  <h2 class="val-title h-light">Our <b>Core Values</b></h2>
  <div class="val-l" style="left:16px;top:88px"><h4>Commitment</h4><p>We are dedicated to<br>our client's success</p></div>
  <div class="val-l" style="left:16px;top:145px"><h4>Innovation</h4><p>We are constantly looking for ways<br>to improve efficiency and effectiveness.</p></div>
  <div class="val-l" style="left:16px;top:202px"><h4>Results</h4><p>We motivated, passionate committed<br>to produce the best results for our clients</p></div>
  <svg class="val-icon" style="left:225px;top:88px;background:var(--red)" viewBox="0 0 38 38"><path d="M11 17h4v10h-4z M17 17l4-7c2 0 2 1 2 2l-1 4h5c2 0 2 2 1 3l-2 7c0 1-1 1-2 1h-7z" fill="#fff"/></svg>
  <svg class="val-icon" style="left:274px;top:88px;background:var(--green)" viewBox="0 0 38 38"><path d="M13 10h12v5c0 4-3 7-6 7s-6-3-6-7z" fill="#fff"/><rect x="17" y="22" width="4" height="4" fill="#fff"/><rect x="13" y="26" width="12" height="3" fill="#fff"/></svg>
  <svg class="val-icon" style="left:225px;top:145px;background:var(--sky)" viewBox="0 0 38 38"><circle cx="19" cy="16" r="7" fill="#fff"/><rect x="16" y="22" width="6" height="6" rx="1" fill="#fff"/></svg>
  <svg class="val-icon" style="left:274px;top:145px;background:var(--red)" viewBox="0 0 38 38"><circle cx="14" cy="14" r="3.5" fill="#fff"/><circle cx="24" cy="14" r="3.5" fill="#fff"/><path d="M8 28c0-5 3-8 6-8s6 3 6 8z M18 28c0-5 3-8 6-8s6 3 6 8z" fill="#fff"/></svg>
  <svg class="val-icon" style="left:225px;top:202px;background:var(--green)" viewBox="0 0 38 38"><rect x="11" y="21" width="4" height="7" fill="#fff"/><rect x="17" y="17" width="4" height="11" fill="#fff"/><rect x="23" y="13" width="4" height="15" fill="#fff"/></svg>
  <svg class="val-icon" style="left:274px;top:202px;background:var(--sky)" viewBox="0 0 38 38"><circle cx="19" cy="19" r="9" fill="none" stroke="#fff" stroke-width="3.5" stroke-dasharray="4 2.5"/><circle cx="19" cy="19" r="4" fill="#fff"/></svg>
  <div class="val-r" style="top:88px"><h4>Integrity</h4><p>We are committed to perform with integrity and professionalism.</p></div>
  <div class="val-r" style="top:145px"><h4>Compassion</h4><p>Our team recognizes that selling a business is more than just a financial transaction. We guide and support our clients every step of the way.</p></div>
  <div class="val-r" style="top:202px"><h4>Passion</h4><p>We are passionate about small businesses and entrepreneurship.</p></div>
  <div class="logo small" style="left:14px;top:267px"><span class="name">KEYSTONE</span><span class="sub">BUSINESS ADVISORS</span></div>
  <span class="pgno">12</span>
</section>

<!-- Team -->
<section class="slide col-l row7">
  <div class="svc-top"></div>
  <h2 class="team-title h-light">Our <b>Team</b></h2>
  <div class="member" style="left:33px"><div class="portrait" role="img" aria-label="Team member portrait placeholder"></div><h4>Person Name</h4><div class="role">Job Title Goes Here!</div><p>Lorem ipsum dolor sit amet, at laborum nibh duis mauris. Per ultrices lectus sed metus tristique eu. Diam suspendisse ac ipsum maecenas fermentum, aliquet imperdiet et lobortis.</p></div>
  <div class="member" style="left:195px"><div class="portrait" role="img" aria-label="Team member portrait placeholder"></div><h4>Person Name</h4><div class="role">Job Title Goes Here!</div><p>Lorem ipsum dolor sit amet, at laborum nibh duis mauris. Per ultrices lectus sed metus tristique eu. Diam suspendisse ac ipsum maecenas fermentum, aliquet imperdiet et lobortis.</p></div>
  <div class="member" style="left:357px"><div class="portrait" role="img" aria-label="Team member portrait placeholder"></div><h4>Person Name</h4><div class="role">Job Title Goes Here!</div><p>Lorem ipsum dolor sit amet, at laborum nibh duis mauris. Per ultrices lectus sed metus tristique eu. Diam suspendisse ac ipsum maecenas fermentum, aliquet imperdiet et lobortis.</p></div>
  <div class="logo small" style="left:14px;top:267px"><span class="name">KEYSTONE</span><span class="sub">BUSINESS ADVISORS</span></div>
  <span class="pgno">13</span>
</section>

<!-- Ready to partner -->
<section class="slide col-r row7">
  <div class="photo" role="img" aria-label="Photo of a handshake with a faint hexagon network overlay" style="left:37px;top:0;width:236px;height:238px;background:linear-gradient(120deg,#2d4f7e,#8aa0bb 40%,#dfe4ea 70%,#b6c2d0)"></div>
  <h2 class="feat-title h-display" style="left:313px;top:68px">Ready to partner<br>with us?</h2>
  <p class="feat-text" style="left:313px;top:120px;width:190px">Book a time that works for you for a confidential consultation with one of our business brokers. We are looking forward to talking with you about how we can help you to achieve your goals and successfully exit your business.</p>
  <div class="logo small" style="left:14px;top:267px"><span class="name">KEYSTONE</span><span class="sub">BUSINESS ADVISORS</span></div>
  <span class="pgno">14</span>
</section>

<!-- Contact -->
<section class="slide slide-contact">
  <div class="photo" role="img" aria-label="Faint navy-tinted office photo" style="inset:0;background:linear-gradient(150deg,#1c3a68,#15315e 55%,#123058)"></div>
  <div class="logo white" style="left:62px;top:138px"><span class="name" style="font-size:17px">KEYSTONE</span><span class="sub" style="font-size:6.4px">BUSINESS ADVISORS</span></div>
  <h3 class="ct-head abs" style="left:216px;top:44px">Contact Us</h3>
  <div class="office" style="left:216px;top:80px"><h5>Oakland Office</h5><p>4120 Harbor Point Rd.<br>Ste# 110<br>Oakland, CA 94600</p></div>
  <div class="office" style="left:216px;top:138px"><h5>Dublin Office</h5><p>2250 Meadow Ln.<br>#140<br>Dublin, CA 94500</p></div>
  <div class="office" style="left:216px;top:196px"><h5>Walnut Creek</h5><p>318 Orchard Valley Rd. Suite C12<br>Walnut Creek, CA 94500</p><p>925-555-0148<br>Fax: 925-555-0149</p></div>
  <div class="office" style="left:359px;top:42px"><h5>Sacramento Office</h5><p>775 Riverbend Way<br>Ste#310<br>Sacramento, CA 95800</p></div>
  <div class="office" style="left:359px;top:101px"><h5>San Francisco Office</h5><p>980 Lantern St.<br>Ste# 402<br>San Francisco, CA 94100</p></div>
  <div class="office" style="left:359px;top:160px"><h5>Southern California</h5><p>5400 Canyon Crest Blvd, Ste# 207<br>Encino, CA 91400<br>661-555-0172</p><p>812 W. Juniper Ave.<br>#6 Lancaster, CA 93500<br>818-555-0190<br>Fax: 661-555-0191</p></div>
</section>

</body>
</html>
```